" ELA NAO FOI ABERTA AINDA MAS SERA EM 20 DIAS. A VARTEMI - uma empresa especializada na prestação de serviços terceirizados integrados, auxiliando nossos clientes a reduzir custos indiretos, focar em seu negócio principal, sem se preocupar com serviços de apoio, como limpeza, copa, portaria, segurança, administrativo, zeladoria, telefonia e recepção. Uma empresa ou Condomínio apresenta necessidades diversas para se manter operando de maneira lucrativa e segura. Antes, cada negócio precisava atender às demandas por meio de sua infraestrutura interna. Mas uma opção vantajosa vem crescendo no mercado e merece destaque atualmente: a terceirização de atividades "

```html
<!DOCTYPE html>
<html lang="pt-BR">
<head>
<meta charset="utf-8">
<title>VARTEMI – Envelope</title>
<link href="https://fonts.googleapis.com/css2?family=Montserrat:wght@400;600;700&display=swap" rel="stylesheet">
<style>
  :root{
    --stage:#2a2a2c;
    --paper-top:#ffffff;
    --paper-bottom:#dcdde0;
    --ink-dark:#0c0c0d;
    --ink-mid:#1b1b1d;
    --gold:#c9a449;
    --blue:#2f4fa8;
    --text:#3a3a3c;
    --strip:#c9cacd;
  }
  *{margin:0;padding:0;box-sizing:border-box}
  html,body{width:1200px;height:1200px;overflow:hidden;background:var(--stage);font-family:"Montserrat",sans-serif}
  .canvas{position:relative;width:1200px;height:1200px}

  .envelope{position:absolute;top:283px;width:509px;height:725px;overflow:hidden}
  .envelope--front{left:84px;background:linear-gradient(180deg,var(--paper-top) 0%,#f2f2f3 55%,var(--paper-bottom) 100%)}
  .envelope--back{left:612px;background:radial-gradient(ellipse at 45% 35%,#2a2a2c 0%,var(--ink-mid) 45%,var(--ink-dark) 100%)}

  .flap{position:absolute;top:0;left:0;width:509px;height:100px}
  .brand{position:absolute;left:0;right:0;text-align:center;font-weight:700;letter-spacing:.12em;color:var(--gold)}
  .brand--flap{top:34px;font-size:26px}
  .brand--footer{top:560px;font-size:24px;color:var(--blue)}
  .brand--back{top:610px;font-size:52px}
  .brand-dot{display:inline-block;width:.42em;height:.42em;border-radius:50%;background:currentColor;margin-right:.35em;vertical-align:.12em}

  .watermark{position:absolute;left:0;right:0;text-align:center;font-weight:700;letter-spacing:.08em;pointer-events:none}
  .watermark--front{top:340px;font-size:92px;color:rgba(0,0,0,.05)}
  .watermark--back{top:300px;font-size:108px;color:rgba(255,255,255,.04)}

  .contact{position:absolute;top:640px;left:14px;right:14px;display:flex;align-items:flex-start;gap:22px;font-size:9px;line-height:1.45;color:var(--text)}
  .contact-rule{width:28px;height:2px;background:var(--blue);margin-top:5px;flex:none}
  .contact-item{display:flex;align-items:center;gap:5px}
  .contact-item svg{flex:none}

  .strip{position:absolute;left:0;bottom:0;width:509px;height:34px}
</style>
</head>
<body>
<main class="canvas">

  <section class="envelope envelope--front" aria-label="Envelope, frente">
    <svg class="flap" viewBox="0 0 509 100" aria-hidden="true">
      <defs>
        <linearGradient id="flapFill" x1="0" y1="0" x2="0" y2="1">
          <stop offset="0" stop-color="#1e1e20"/><stop offset="1" stop-color="#060607"/>
        </linearGradient>
      </defs>
      <path d="M0 0H509V62Q509 100 471 100H38Q0 100 0 62Z" fill="url(#flapFill)"/>
    </svg>
    <div class="brand brand--flap"><span class="brand-dot"></span>VARTEMI</div>

    <div class="watermark watermark--front">VARTEMI</div>

    <div class="brand brand--footer">VARTEMI</div>

    <div class="contact">
      <span class="contact-rule"></span>
      <div class="contact-address">Rua das Acácias 418, Sala 2<br>Centro, Campinas - SP<br>CEP 13010-100</div>
      <div class="contact-item">
        <svg width="10" height="8" viewBox="0 0 10 8"><rect x=".5" y=".5" width="9" height="7" fill="none" stroke="#3a3a3c"/><path d="M.5 .5L5 4.5L9.5 .5" fill="none" stroke="#3a3a3c"/></svg>
        contato@vartemi.com.br
      </div>
      <div class="contact-item">
        <svg width="8" height="10" viewBox="0 0 8 10"><rect x=".5" y=".5" width="7" height="9" rx="1.5" fill="none" stroke="#3a3a3c"/><circle cx="4" cy="8" r=".7" fill="#3a3a3c"/></svg>
        (19) 3456-7890
      </div>
    </div>

    <svg class="strip" viewBox="0 0 509 34" aria-hidden="true">
      <path d="M0 14H200Q215 14 222 22H287Q294 14 309 14H509V34H0Z" fill="var(--strip)"/>
      <line x1="0" y1="14" x2="509" y2="14" stroke="#b4b5b8" stroke-width="1"/>
    </svg>
  </section>

  <section class="envelope envelope--back" aria-label="Envelope, verso">
    <div class="watermark watermark--back">VARTEMI</div>
    <div class="brand brand--back"><span class="brand-dot"></span>VARTEMI</div>
    <svg class="strip" viewBox="0 0 509 34" aria-hidden="true">
      <defs>
        <linearGradient id="backStrip" x1="0" y1="0" x2="1" y2="0">
          <stop offset="0" stop-color="#3a3a3c"/><stop offset=".5" stop-color="#9a9b9e"/><stop offset="1" stop-color="#3a3a3c"/>
        </linearGradient>
      </defs>
      <path d="M0 20H200Q215 20 222 12H287Q294 20 309 20H509V34H0Z" fill="url(#backStrip)"/>
    </svg>
  </section>

</main>
</body>
</html>
```